TorvaMax needs app design - Social app for a party on a budget

We need a design for our app called "TorvaMax", TorvaMax is an essential application that showcases the finest clubs in the city. The primary objective of the app is to provide users with insights into club ratings and beer prices, enabling them to locate the most cost-effective beer near their current location. You as a user will also have ability to rate different Additionally, users can view posts and images from various patrons, offering glimpses into the ambiance of the establishments to determine if they meet their preferences and requirements.

We imagine Torvamax having a "gamification app desigin" as partying is like a game, you experience new adventures and take on new quests.
Allthough we are open for different designs, surprise us.

Keyfeatures:
1 - Splash/Login Page:
Allow users to log in or sign up using Plimbo, Snapvera, or Chatterloo credentials.
2 - Home Page/Announcements:
Display user-generated posts from different clubs and pubs, showcasing crowd levels and overall enjoyment.
Enable users to like posts, with sorting based on likes and proximity.
Access announcements from establishments about upcoming events, entrance fees, and performances.
3 - Search Page:
Provide a map displaying nearby pubs and clubs, with basic information such as rating, beer prices, and operating hours.
4 - List Page:
Present a comprehensive list of nearby clubs and pubs, sorted initially by rating.
Allow users to sort by beer prices, location, and other criteria.
Enable users to rate establishments using a 1-5 star system, with monthly winners prominently featured on the announcement page.
5 - My page:
Allow users to revisit and upload memories, including pictures, locations, dates, and times.
Provide an option to repost pictures on Snapvera.
Feature a "Refer a Friend" button for users to earn complimentary memberships by referring friends who complete the registration process.

As mentioned these are only key features we imagine this app should have, feel free to play around with the design.

18

• Key features meantioned in project description

```html
<!DOCTYPE html>
<html lang="en">
<head>
<meta charset="utf-8">
<title>TorvaMax – app screens</title>
<link rel="stylesheet" href="https://fonts.googleapis.com/css2?family=Source+Sans+3:wght@400;600;700&display=swap">
<style>
:root{
  --bg:#1c1a2f;
  --purple:#6446e3;
  --purple-deep:#5133c8;
  --violet:#9a3fe0;
  --card-violet:#9b55ea;
  --login:#4b2a86;
  --yellow:#ffd60a;
  --ink:#2b2a38;
  --muted:#676776;
  --line:#e6e6ec;
  --nav:#4a33c3;
  --white:#ffffff;
}
*{box-sizing:border-box;margin:0;padding:0}
html,body{width:1200px;height:433px;overflow:hidden;background:var(--bg);font-family:"Source Sans 3",sans-serif;color:var(--ink)}
.canvas{position:relative;width:1200px;height:433px}
.screen{position:absolute;top:50px;width:158px;height:343px;overflow:hidden;background:var(--white)}
.screen--purple{background:radial-gradient(120% 60% at 20% 75%,var(--purple-deep) 0 45%,transparent 46%),var(--purple)}
.splash{left:68px;top:56px;width:156px;height:338px;border-radius:16px}
.splash__title{position:absolute;top:150px;width:100%;text-align:center;color:var(--white);font-weight:700;font-size:30px;letter-spacing:.3px}

/* header */
.header{position:absolute;top:17px;left:0;width:100%;height:16px;text-align:center}
.header__title{font-weight:700;font-size:12px;color:var(--violet);line-height:16px}
.screen--purple .header__title{color:var(--white)}
.header__icon{position:absolute;top:4px;width:8px;height:8px}
.header__icon--left{left:10px}
.header__icon--right{right:10px}

/* tabs */
.tabs{position:absolute;top:45px;left:12px;width:135px;display:flex;gap:4px}
.tab{flex:1;height:19px;border:1px solid var(--yellow);border-radius:2px;font-size:6.5px;font-weight:600;display:flex;align-items:center;justify-content:center;color:var(--ink)}
.tab--active{background:var(--yellow)}

/* nav */
.nav{position:absolute;left:0;bottom:0;width:100%;height:25px;background:var(--nav);display:flex}
.nav__item{flex:1;display:flex;flex-direction:column;align-items:center;justify-content:center;gap:1px;color:var(--white);font-size:5.5px}
.nav__item svg{width:9px;height:9px;fill:currentColor}
.nav__item--active{color:var(--yellow)}

/* login */
.login__title{position:absolute;top:72px;width:100%;text-align:center;color:var(--white);font-weight:700;font-size:20px}
.login__lede{position:absolute;top:98px;left:20px;right:12px;text-align:center;color:var(--white);font-size:6.3px;line-height:10px}
.login__card{position:absolute;top:132px;left:14px;width:135px;height:121px;border-radius:7px;background:var(--card-violet)}
.btn{position:absolute;left:10px;width:116px;height:19px;border-radius:2px;display:flex;align-items:center;justify-content:center;font-size:6.5px;font-weight:600}
.btn--login{top:19px;background:var(--login);color:var(--white)}
.btn--signup{top:43px;background:var(--yellow);color:var(--ink)}
.login__divider{position:absolute;top:75px;left:10px;width:116px;text-align:center;color:var(--white);font-size:6.5px}
.login__divider::before,.login__divider::after{content:"";position:absolute;top:5px;width:30px;height:1px;background:rgba(255,255,255,.35)}
.login__divider::before{left:0}.login__divider::after{right:0}
.socials{position:absolute;top:94px;left:10px;width:116px;display:flex;gap:3px}
.social{flex:1;height:15px;background:var(--white);border-radius:2px;display:flex;align-items:center;justify-content:center;gap:2px;font-size:4.6px;color:var(--ink)}
.social i{width:4px;height:4px;border-radius:50%;background:var(--violet);display:block}

/* post cards */
.post{position:absolute;left:12px;width:135px;height:107px;background:var(--white);border-radius:3px;box-shadow:0 1px 4px rgba(0,0,0,.12);overflow:hidden}
.post__photo{height:76px;border-radius:3px 3px 0 0}
.photo--a{background:linear-gradient(135deg,#3a1c2a,#8a4a3a 45%,#2a1520)}
.photo--b{background:linear-gradient(135deg,#2a1a18,#9a5a3a 50%,#4a2a28)}
.photo--c{background:linear-gradient(135deg,#2a2440,#6a4a70)}
.post__name{position:absolute;left:8px;top:81px;font-size:7.5px;font-weight:600}
.post__meta{position:absolute;left:8px;top:92px;font-size:5.6px;color:var(--muted)}
.post__heart{position:absolute;right:12px;top:84px;width:9px;height:8px;fill:#e5243a}
.stars{color:var(--yellow);font-size:5px;letter-spacing:.3px;margin-left:2px;vertical-align:1px}
.stars .off{color:#d8d8dd}

/* announcements */
.note{position:absolute;left:12px;width:135px;background:var(--white);border-radius:3px;box-shadow:0 1px 4px rgba(0,0,0,.12);overflow:hidden}
.note__head{position:relative;height:33px;border-bottom:1px solid var(--line);margin:0 8px}
.avatar{position:absolute;width:20px;height:20px;border-radius:50%;background:#1f1d24}
.note__head .avatar{left:0;top:7px}
.note__name{position:absolute;left:25px;top:7px;font-size:7.5px;font-weight:600}
.note__date{position:absolute;left:25px;top:19px;font-size:5.6px;color:var(--muted)}
.note__body{padding:6px 9px 0 9px;font-size:5.6px;line-height:9px;color:var(--muted)}

/* venue */
.venue__name{position:absolute;top:61px;width:100%;text-align:center;color:var(--white);font-weight:600;font-size:10px}
.venue__stars{position:absolute;top:74px;width:100%;text-align:center}
.venue__facts{position:absolute;top:93px;width:100%;text-align:center;color:var(--white);font-size:6.5px;line-height:10.3px}
.venue__facts b{font-weight:700}
.venue__map{position:absolute;top:132px;left:12px;width:135px;height:150px;border-radius:7px;background:linear-gradient(135deg,#e9ecef 0 40%,#a8d08d 60%,#6fbbe8 85%,#e9ecef)}

/* list */
.place{position:absolute;left:12px;width:135px;height:58px;border-bottom:1px solid var(--line)}
.place .avatar{left:0;top:0}
.place__name{position:absolute;left:24px;top:0;font-size:7.5px;font-weight:600}
.place__meta{position:absolute;left:24px;top:10px;font-size:5.6px;color:var(--muted)}
.place__addr{position:absolute;left:12px;top:24px;width:85px;font-size:5.6px;line-height:9px;color:var(--muted)}
.place__pin{position:absolute;left:5px;top:26px;width:4px;height:5px;fill:var(--violet)}
.place__visit{position:absolute;right:0;top:29px;width:25px;height:13px;background:var(--yellow);border-radius:2px;font-size:6px;font-weight:600;display:flex;align-items:center;justify-content:center}
</style>
</head>
<body>
<svg width="0" height="0" style="position:absolute" aria-hidden="true">
  <symbol id="i-home" viewBox="0 0 10 10"><path d="M5 .6 0 5h1.4v4.4h2.8V6.6h1.6v2.8h2.8V5H10z"/></symbol>
  <symbol id="i-map" viewBox="0 0 10 10"><path d="M0 1.5 3 .5v8l-3 1zM3.5.5l3 1v8l-3-1zM7 1.5l3-1v8l-3 1z"/></symbol>
  <symbol id="i-menu" viewBox="0 0 10 10"><path d="M0 1h10v1.4H0zM0 4.3h10v1.4H0zM0 7.6h10V9H0z"/></symbol>
  <symbol id="i-user" viewBox="0 0 10 10"><circle cx="5" cy="2.6" r="2.3"/><path d="M.6 10c0-3 2-4.4 4.4-4.4S9.4 7 9.4 10z"/></symbol>
  <symbol id="i-heart" viewBox="0 0 10 9"><path d="M5 9 .9 4.9A2.5 2.5 0 0 1 5 1.5a2.5 2.5 0 0 1 4.1 3.4z"/></symbol>
  <symbol id="i-pin" viewBox="0 0 4 5"><path d="M2 0a2 2 0 0 0-2 2c0 1.4 2 3 2 3s2-1.6 2-3a2 2 0 0 0-2-2zm0 2.8A.8.8 0 1 1 2 1.2a.8.8 0 0 1 0 1.6z"/></symbol>
  <symbol id="i-back" viewBox="0 0 8 8"><path d="M5.5 .5 2 4l3.5 3.5" fill="none" stroke="currentColor" stroke-width="1.2"/></symbol>
  <symbol id="i-search" viewBox="0 0 8 8"><circle cx="3.3" cy="3.3" r="2.5" fill="none" stroke="currentColor" stroke-width=".9"/><path d="m5.2 5.2 2.3 2.3" stroke="currentColor" stroke-width=".9"/></symbol>
  <symbol id="i-filter" viewBox="0 0 8 8"><path d="M.5.8h7L4.7 4.2v3L3.3 6.4V4.2z" fill="none" stroke="currentColor" stroke-width=".8"/></symbol>
</svg>

<main class="canvas">

  <!-- Splash -->
  <section class="screen screen--purple splash">
    <h1 class="splash__title">TorvaMax</h1>
  </section>

  <!-- Login -->
  <section class="screen screen--purple" style="left:290px">
    <h2 class="login__title">TorvaMax</h2>
    <p class="login__lede">Lorem ipsum dolor sit amet, consectetur adipiscing elit, sed do eiusmod tempor</p>
    <div class="login__card">
      <div class="btn btn--login">Login</div>
      <div class="btn btn--signup">Sign Up</div>
      <p class="login__divider">or connect with</p>
      <div class="socials">
        <span class="social"><i></i>Plimbo</span>
        <span class="social"><i></i>Snapvera</span>
        <span class="social"><i></i>Chatterloo</span>
      </div>
    </div>
  </section>

  <!-- Home: For You -->
  <section class="screen" style="left:468px">
    <header class="header">
      <svg class="header__icon header__icon--left" style="color:var(--ink)"><use href="#i-back"/></svg>
      <span class="header__title">TorvaMax</span>
    </header>
    <div class="tabs"><span class="tab tab--active">For You</span><span class="tab">Announcements</span></div>
    <article class="post" style="top:78px">
      <div class="post__photo photo--a" role="img" aria-label="Photo of friends toasting drinks in a club"></div>
      <span class="post__name">Kobberhall <span class="stars">★★★★★</span></span>
      <span class="post__meta">Entrance: 100 Kr, 80Kr</span>
      <svg class="post__heart"><use href="#i-heart"/></svg>
    </article>
    <article class="post" style="top:192px">
      <div class="post__photo photo--b" role="img" aria-label="Photo of a crowd partying together"></div>
      <span class="post__name">Lanternbar <span class="stars">★★★★★</span></span>
      <span class="post__meta">Entrance: 100 Kr, 80Kr</span>
      <svg class="post__heart"><use href="#i-heart"/></svg>
    </article>
    <article class="post" style="top:306px">
      <div class="post__photo photo--c" role="img" aria-label="Photo of a dance floor with raised hands"></div>
    </article>
    <nav class="nav">
      <span class="nav__item nav__item--active"><svg><use href="#i-home"/></svg>Home</span>
      <span class="nav__item"><svg><use href="#i-map"/></svg>Map</span>
      <span class="nav__item"><svg><use href="#i-menu"/></svg>Menu</span>
      <span class="nav__item"><svg><use href="#i-user"/></svg>Account</span>
    </nav>
  </section>

  <!-- Home: Announcements -->
  <section class="screen" style="left:640px">
    <header class="header">
      <svg class="header__icon header__icon--left" style="color:var(--ink)"><use href="#i-back"/></svg>
      <span class="header__title">TorvaMax</span>
    </header>
    <div class="tabs"><span class="tab">For You</span><span class="tab tab--active">Announcements</span></div>
    <article class="note" style="top:78px;height:92px">
      <div class="note__head"><span class="avatar"></span><span class="note__name">Kobberhall <span class="stars">★★★★★</span></span><span class="note__date">June 23, 2024</span></div>
      <p class="note__body">Kobberhall extends complimentary admission until 22:00, with a beer price set at 60kr. Please note, the minimum age for entry is 20 years old. DJ Vantro will be headlining tonight's entertainment.</p>
    </article>
    <article class="note" style="top:178px;height:93px">
      <div class="note__head"><span class="avatar"></span><span class="note__name">Lanternbar <span class="stars">★★★★★</span></span><span class="note__date">June 23, 2024</span></div>
      <p class="note__body">Lanternbar is offering complimentary admission until 23:00, with beer priced at 59kr. Kindly be advised that the minimum age for entry is 18 years old. MC Korlo will be headlining tonight's entertainment.</p>
    </article>
    <article class="note" style="top:278px;height:60px">
      <div class="note__head"><span class="avatar"></span><span class="note__name">Lorem Ipsum <span class="stars">★★★★★</span></span><span class="note__date">June 23, 2024</span></div>
    </article>
    <nav class="nav">
      <span class="nav__item nav__item--active"><svg><use href="#i-home"/></svg>Home</span>
      <span class="nav__item"><svg><use href="#i-map"/></svg>Map</span>
      <span class="nav__item"><svg><use href="#i-menu"/></svg>Menu</span>
      <span class="nav__item"><svg><use href="#i-user"/></svg>Account</span>
    </nav>
  </section>

  <!-- Map / venue -->
  <section class="screen screen--purple" style="left:810px">
    <header class="header">
      <svg class="header__icon header__icon--left" style="color:var(--white)"><use href="#i-back"/></svg>
      <span class="header__title">TorvaMax</span>
    </header>
    <h3 class="venue__name">Kobberhall</h3>
    <div class="venue__stars"><span class="stars" style="font-size:6px">★★★★★</span></div>
    <p class="venue__facts">Opening hours: <b>20:00-03:00</b><br>Age: <b>21+</b><br>Beer coast: <b>80Kr</b></p>
    <div class="venue__map" role="img" aria-label="City map with the venue location marked near the river"></div>
    <nav class="nav">
      <span class="nav__item"><svg><use href="#i-home"/></svg>Home</span>
      <span class="nav__item nav__item--active"><svg><use href="#i-map"/></svg>Map</span>
      <span class="nav__item"><svg><use href="#i-menu"/></svg>Menu</span>
      <span class="nav__item"><svg><use href="#i-user"/></svg>Account</span>
    </nav>
  </section>

  <!-- List -->
  <section class="screen" style="left:980px">
    <header class="header">
      <svg class="header__icon header__icon--left" style="color:var(--muted)"><use href="#i-search"/></svg>
      <span class="header__title">TorvaMax</span>
      <svg class="header__icon header__icon--right" style="color:var(--muted)"><use href="#i-filter"/></svg>
    </header>
    <article class="place" style="top:53px">
      <span class="avatar"></span><span class="place__name">Lanternbar <span class="stars">★★★★★</span></span>
      <span class="place__meta">Entrance:0 Kr | Beer 69 Kr</span>
      <svg class="place__pin"><use href="#i-pin"/></svg>
      <p class="place__addr">Unit 12 Pinecrest Row, Eastvale, CO 80014-2210</p>
      <span class="place__visit">Visit</span>
    </article>
    <article class="place" style="top:110px">
      <span class="avatar"></span><span class="place__name">Kobberhall <span class="stars">★★★★★</span></span>
      <span class="place__meta">Entrance:100 Kr | Beer 69 Kr</span>
      <svg class="place__pin"><use href="#i-pin"/></svg>
      <p class="place__addr">Unit 12 Pinecrest Row, Eastvale, CO 80014-2210</p>
      <span class="place__visit">Visit</span>
    </article>
    <article class="place" style="top:169px">
      <span class="avatar"></span><span class="place__name">Marina BAR <span class="stars">★★★★★</span></span>
      <span class="place__meta">Entrance:100 Kr | Beer 69 Kr</span>
      <svg class="place__pin"><use href="#i-pin"/></svg>
      <p class="place__addr">Unit 12 Pinecrest Row, Eastvale, CO 80014-2210</p>
      <span class="place__visit">Visit</span>
    </article>
    <article class="place" style="top:226px">
      <span class="avatar"></span><span class="place__name">Blikk <span class="stars">★★★★<span class="off">★</span></span></span>
      <span class="place__meta">Entrance:100 Kr | Beer 69 Kr</span>
      <svg class="place__pin"><use href="#i-pin"/></svg>
      <p class="place__addr">Unit 12 Pinecrest Row, Eastvale, CO 80014-2210</p>
      <span class="place__visit">Visit</span>
    </article>
    <article class="place" style="top:283px">
      <span class="avatar"></span><span class="place__name">Fjordkroa <span class="stars">★★★<span class="off">★★</span></span></span>
      <span class="place__meta">Entrance:100 Kr | Beer 69 Kr</span>
      <svg class="place__pin"><use href="#i-pin"/></svg>
      <p class="place__addr">Unit 12 Pinecrest Row, Eastvale, CO 80014-2210</p>
      <span class="place__visit">Visit</span>
    </article>
    <nav class="nav">
      <span class="nav__item"><svg><use href="#i-home"/></svg>Home</span>
      <span class="nav__item"><svg><use href="#i-map"/></svg>Map</span>
      <span class="nav__item nav__item--active"><svg><use href="#i-menu"/></svg>Menu</span>
      <span class="nav__item"><svg><use href="#i-user"/></svg>Account</span>
    </nav>
  </section>

</main>
</body>
</html>
```